Tag design needed for wall art products

We need to design a tag for wall art products, which are Canvas, wood art, and rolling canvas.

The Tag need to be classical which means not too colorful, all information in the file (1pic) need to be included such as brand name, company website.

The side of tag need to be same as Kavrix 6 or Kavrix 7 with a hole on the top.
Updates

More designs are required!

Target Market(s)

US Market

Industry/Entity Type

Home And Garden

Requirements
Must have
• ART.DECORATION
• BRENDITH&TULIVARE
• 1978
• WWW.TULIVAREHUE.EXAMPLE
• HONGKONG AUSTRALIA CHINA

```html
<!DOCTYPE html>
<html lang="en">
<head>
<meta charset="utf-8">
<title>Brendith &amp; Tulivare — Hang Tags</title>
<link rel="stylesheet" href="https://fonts.googleapis.com/css2?family=Playfair+Display:wght@400;700&family=Barlow:wght@300;400&display=swap">
<style>
  :root {
    --backdrop: #dedede;
    --ink-dark: #161615;
    --paper-light: #f6f5f1;
    --gold: #b98a3e;
    --gold-light: #e2bd74;
    --gold-deep: #8a6224;
  }
  * { margin: 0; padding: 0; box-sizing: border-box; }
  html, body {
    width: 1200px;
    height: 960px;
    overflow: hidden;
    background: var(--backdrop);
  }
  .sheet {
    position: relative;
    width: 1200px;
    height: 960px;
  }
  .tag {
    position: absolute;
    top: 122px;
    width: 402px;
    height: 717px;
    color: var(--gold);
  }
  .tag--dark { left: 153px; background: var(--ink-dark); }
  .tag--light { left: 645px; background: var(--paper-light); }

  .tag__frame {
    position: absolute;
    inset: 10px;
    border: 2px solid var(--gold);
  }
  .tag__frame::after {
    content: "";
    position: absolute;
    inset: 5px;
    border: 1px solid var(--gold);
  }

  .tag__hole {
    position: absolute;
    left: 50%;
    top: 33px;
    width: 112px;
    height: 112px;
    transform: translateX(-50%);
  }

  .tag__tagline {
    position: absolute;
    left: 0;
    right: 0;
    top: 160px;
    text-align: center;
    font-family: "Barlow", sans-serif;
    font-weight: 300;
    font-size: 20px;
    letter-spacing: 3px;
  }

  .tag__flourish {
    position: absolute;
    left: 50%;
    transform: translateX(-50%);
    border-radius: 4px;
    background: linear-gradient(90deg, var(--gold-deep), var(--gold-light) 50%, var(--gold-deep));
    opacity: 0.85;
  }
  .tag__flourish--top { top: 203px; width: 254px; height: 36px; }
  .tag__flourish--bottom { top: 602px; width: 314px; height: 38px; }

  .tag__ornament {
    position: absolute;
    left: 50%;
    top: 428px;
    width: 180px;
    height: 118px;
    transform: translateX(-50%);
    border-radius: 6px;
    background: radial-gradient(ellipse at center, var(--gold-light), var(--gold-deep));
    opacity: 0.85;
  }

  .tag__brand {
    position: absolute;
    left: 0;
    right: 0;
    top: 250px;
    text-align: center;
    font-family: "Playfair Display", serif;
    font-weight: 400;
    font-size: 41px;
    line-height: 44px;
    letter-spacing: 0.5px;
  }
  .tag__rule {
    position: absolute;
    left: 50%;
    top: 358px;
    width: 136px;
    height: 2px;
    transform: translateX(-50%);
    background: var(--gold);
  }
  .tag__rule::after {
    content: "";
    position: absolute;
    left: 50%;
    top: -2px;
    width: 40px;
    height: 5px;
    transform: translateX(-50%);
    background: var(--gold);
    border-radius: 3px;
  }
  .tag__year {
    position: absolute;
    left: 0;
    right: 0;
    top: 376px;
    text-align: center;
    font-family: "Playfair Display", serif;
    font-size: 32px;
  }
  .tag__line {
    position: absolute;
    left: 0;
    right: 0;
    top: 558px;
    text-align: center;
    font-family: "Playfair Display", serif;
    font-weight: 700;
    font-size: 25px;
    letter-spacing: 1px;
  }
  .tag__line sup { font-size: 14px; font-weight: 400; }

  .tag__web,
  .tag__regions {
    position: absolute;
    left: 0;
    right: 0;
    text-align: center;
    font-family: "Barlow", sans-serif;
    font-weight: 400;
  }
  .tag__web { top: 648px; font-size: 13px; letter-spacing: 1.5px; }
  .tag__regions { top: 670px; font-size: 11px; letter-spacing: 3px; }
</style>
</head>
<body>
<main class="sheet">

  <article class="tag tag--dark">
    <div class="tag__frame"></div>
    <svg class="tag__hole" viewBox="0 0 112 112" aria-hidden="true">
      <circle cx="56" cy="56" r="8" fill="var(--backdrop)" stroke="var(--gold)" stroke-width="2"/>
    </svg>
    <div class="tag__tagline">ART·DECORATION</div>
    <div class="tag__flourish tag__flourish--top" role="img" aria-label="Gold engraved scroll flourish"></div>
    <h1 class="tag__brand">BRENDITH<br>&amp;TULIVARE</h1>
    <div class="tag__rule"></div>
    <div class="tag__year">1978</div>
    <div class="tag__ornament" role="img" aria-label="Gold engraved symmetrical crest ornament"></div>
    <div class="tag__line">VESPERTINT<sup>™</sup></div>
    <div class="tag__flourish tag__flourish--bottom" role="img" aria-label="Gold engraved foliage border ornament"></div>
    <div class="tag__web">WWW.TULIVAREHUE.EXAMPLE</div>
    <div class="tag__regions">HONGKONG · AUSTRALIA · CHINA</div>
  </article>

  <article class="tag tag--light">
    <div class="tag__frame"></div>
    <svg class="tag__hole" viewBox="0 0 112 112" aria-hidden="true">
      <circle cx="56" cy="56" r="8" fill="var(--backdrop)" stroke="var(--gold)" stroke-width="2"/>
    </svg>
    <div class="tag__tagline">ART·DECORATION</div>
    <div class="tag__flourish tag__flourish--top" role="img" aria-label="Gold engraved scroll flourish"></div>
    <h1 class="tag__brand">BRENDITH<br>&amp;TULIVARE</h1>
    <div class="tag__rule"></div>
    <div class="tag__year">1978</div>
    <div class="tag__ornament" role="img" aria-label="Gold engraved symmetrical crest ornament"></div>
    <div class="tag__line">VESPERTINT<sup>™</sup></div>
    <div class="tag__flourish tag__flourish--bottom" role="img" aria-label="Gold engraved foliage border ornament"></div>
    <div class="tag__web">WWW.TULIVAREHUE.EXAMPLE</div>
    <div class="tag__regions">HONGKONG · AUSTRALIA · CHINA</div>
  </article>

</main>
</body>
</html>
```